Design a PSD Brochure Template

We need a PSD design template for a product catalogue.

Needs to be A4 horizontal/landscape.

Please design a page similar layout to the attached and include on page:
- front page Design
- our logo
- basic footer with email address, phone number and website
- Basic border/design

There will be 5-6 different pages that need to be designed once freelancer is awarded

```html
<!DOCTYPE html>
<html lang="en">
<head>
<meta charset="utf-8">
<title>Sourceline Supply – Company Profile</title>
<link href="https://fonts.googleapis.com/css2?family=Montserrat:wght@400;600;700&family=Oswald:wght@500;700&display=swap" rel="stylesheet">
<style>
  :root{
    --bg:#e6e6e6;
    --navy:#0d3a73;
    --blue:#1e6fc4;
    --sky:#4a9be0;
    --ink:#3a3a3a;
    --paper:#ffffff;
    --ring-grey:#dcdde0;
    --cane:#d9b98c;
    --cream:#ece4d4;
  }
  *{box-sizing:border-box;margin:0;padding:0}
  html,body{width:1200px;height:900px;overflow:hidden;background:var(--bg)}
  body{font-family:"Montserrat",sans-serif;position:relative}
  .spread{position:absolute;left:40px;top:170px;width:1120px;height:560px;display:flex;box-shadow:0 6px 18px rgba(0,0,0,.18)}
  .page{position:relative;width:560px;height:560px;background:var(--paper);overflow:hidden}

  /* back page */
  .contact-band{position:absolute;left:0;top:0;width:255px;height:560px;background:var(--navy);color:#fff;padding:300px 0 0 26px}
  .contact-title{font-size:18px;font-weight:600;letter-spacing:.5px;margin-bottom:14px}
  .contact-list{list-style:none;border-left:1px solid rgba(255,255,255,.6);margin-left:7px}
  .contact-list li{display:flex;align-items:center;gap:8px;font-size:12px;margin:0 0 12px -8px;white-space:nowrap}
  .contact-list svg{width:16px;height:16px;flex:none;background:var(--navy)}
  .social{display:flex;gap:12px;margin-top:26px;margin-left:36px}
  .social span{width:15px;height:15px;border-radius:50%;background:#fff}
  .photo-top{position:absolute;left:255px;top:0;width:305px;height:280px;
    background:
      radial-gradient(ellipse 90px 110px at 50% 48%,var(--cream) 0%,rgba(236,228,212,.6) 45%,rgba(236,228,212,0) 100%),
      linear-gradient(160deg,#f5f5f5,#e3e3e3)}
  .photo-bottom{position:absolute;left:255px;top:280px;width:305px;height:280px;
    background:
      radial-gradient(ellipse 55px 95px at 22% 55%,rgba(217,185,140,.75),rgba(217,185,140,0) 100%),
      radial-gradient(ellipse 55px 95px at 52% 45%,rgba(217,185,140,.75),rgba(217,185,140,0) 100%),
      radial-gradient(ellipse 55px 95px at 80% 38%,rgba(200,150,110,.7),rgba(200,150,110,0) 100%),
      linear-gradient(180deg,#fbfbfb,#f2eee8)}

  /* cover */
  .cover{border-left:1px solid #d9d9d9}
  .cover-art{position:absolute;inset:0}
  .cover-photo{position:absolute;border-radius:50%}
  .cover-photo--main{left:320px;top:70px;width:220px;height:220px;
    background:radial-gradient(ellipse 60px 80px at 50% 50%,var(--cane),rgba(217,185,140,0) 100%),radial-gradient(circle,#faf7f2,#eee7dc)}
  .cover-photo--small{left:262px;top:202px;width:76px;height:76px;
    background:radial-gradient(ellipse 20px 26px at 50% 50%,#b59a7a,rgba(181,154,122,0) 100%),radial-gradient(circle,#f5f3ef,#e2ddd5)}
  .brand{position:absolute;left:46px;top:112px;display:flex;align-items:center;gap:10px}
  .brand-mark{width:30px;height:30px;border-radius:50%;background:var(--navy)}
  .brand-name{font-weight:700;font-size:17px;color:var(--navy);letter-spacing:.6px;line-height:1.05}
  .title-block{position:absolute;left:150px;top:290px;width:215px}
  .title-kicker{font-family:"Oswald",sans-serif;font-weight:500;font-size:14px;color:var(--blue);letter-spacing:.5px;line-height:1.1}
  .title-main{font-family:"Oswald",sans-serif;font-weight:700;font-size:24px;color:var(--ink);line-height:1}
  .title-year{display:block;color:var(--blue);font-size:32px;line-height:1}
  .title-body{font-size:6.5px;line-height:1.45;color:var(--ink);margin-top:6px;font-weight:600}
</style>
</head>
<body>
  <main class="spread">
    <section class="page back-page">
      <div class="photo-top" role="img" aria-label="Photo of a white folding wooden chair with a cushioned seat"></div>
      <div class="photo-bottom" role="img" aria-label="Photo of three rattan bistro chairs with woven seats and backs"></div>
      <div class="contact-band">
        <h2 class="contact-title">CONTACT US</h2>
        <ul class="contact-list">
          <li>
            <svg viewBox="0 0 16 16" fill="none" stroke="#fff" stroke-width="1.3"><rect x="1.5" y="3.5" width="13" height="9"/><path d="M1.5 3.5l6.5 5 6.5-5"/></svg>
            orders@sourceline.example
          </li>
          <li>
            <svg viewBox="0 0 16 16" fill="none" stroke="#fff" stroke-width="1.3"><path d="M4 2l2 3-1.3 1.3a8 8 0 0 0 5 5L11 10l3 2-1.5 2.2C7.5 14 2 8.5 1.8 3.5z"/></svg>
            +27 71 555 0142
          </li>
          <li>
            <svg viewBox="0 0 16 16" fill="#fff"><path d="M8 1a5 5 0 0 0-5 5c0 4 5 9 5 9s5-5 5-9a5 5 0 0 0-5-5zm0 7a2 2 0 1 1 0-4 2 2 0 0 1 0 4z"/></svg>
            Plot nr. 14 Kleinvallei
          </li>
        </ul>
        <div class="social" aria-label="Social channels"><span></span><span></span><span></span></div>
      </div>
    </section>

    <section class="page cover">
      <svg class="cover-art" viewBox="0 0 560 560" aria-hidden="true">
        <polygon points="330,0 560,0 560,60 470,40" fill="#2f86d6"/>
        <polygon points="400,0 560,0 560,150 500,60" fill="var(--sky)" opacity=".8"/>
        <polygon points="470,40 560,60 560,150" fill="#9cc8ef" opacity=".7"/>
        <circle cx="430" cy="180" r="135" fill="var(--paper)" stroke="var(--ring-grey)" stroke-width="14"/>
        <circle cx="430" cy="180" r="120" fill="none" stroke="var(--navy)" stroke-width="20"/>
        <circle cx="300" cy="240" r="42" fill="var(--paper)" stroke="var(--ring-grey)" stroke-width="8"/>
      </svg>
      <div class="cover-photo cover-photo--main" role="img" aria-label="Photo of a rattan armchair with a green and white woven seat"></div>
      <div class="cover-photo cover-photo--small" role="img" aria-label="Photo of a small rattan side chair"></div>

      <div class="brand">
        <span class="brand-mark"></span>
        <span class="brand-name">SOURCELINE<br>SUPPLY</span>
      </div>

      <div class="title-block">
        <p class="title-kicker">COMPANY</p>
        <h1 class="title-main">PROFILE <span class="title-year">2018</span></h1>
        <p class="title-body">We source durable furniture for hotels, cafés and event venues across the region, delivering quality pieces on time and within budget since the year we opened.</p>
      </div>
    </section>
  </main>
</body>
</html>
```